Post card design for ( Interior ) & ( Exterior ) Residential Painting

We need a post card design for interior painting. To get homeowners to call about getting there interior home painted before the end winter comes, to get a clean, quality and no hassle paint job with low odor paints

Some IDEAS:
Exterior Paint Season is Coming to Northern VA and Metro DC!
Have you taken a look around your house this winter? Have you noticed any areas of unwanted moisture, mold or draft? Keeping your house painted and well-maintained on the outside will save money in the future as well. It protects your home from the elements – whether, wind, rain and snow or the strong summer sun.

idea #2
Exterior Paint Makes Your House Last Longer
aintaining a good coat of the correct type of paint on the exterior of your home will help protect your home from the elements and extend the overall life of the structure
idea #3
Rotten Wood and Two Other TOP Reasons for Exterior Paint
We’ll start there – rotten wood – the first reason for exterior paint. If your home or building has decorative wood trim, wood siding or even wood around windows and doors, it could be at risk for rotten or rotting wood. Maintaining a healthy and COMPLETE coat of paint will protect the wood from water damage. Additionally, during a paint project, our team can assess wooden areas and advise if there are any places of concern. For a long-term solution, consider replacing wood trim with vinyl or wood alternatives that stand up to the elements. This can also be done during an exterior paint project.
Idea # 4
Benefits of Using Low-VOC interior Paints
Paints with low-VOC or Zero-VOC are considered healthier options due to the lower amount of toxins they release when applied to a wall. Latex paints are popular low-VOC because they are water based and don’t contain other chemicals you may find in oil-based paints.

Less odor! Because these paints have lower levels of toxins that are released, the paint smell that is associated with a fresh coat of paint is not as strong. Low-VOC would be a great option if you plan on painting a nursery because the smell won’t linger. Although you might not smell it, it is always important to ventilate the room. All paints, even low-VOC have levels of toxicity which are not good to breathe in for long periods of time.

Target Market(s)

single family homes

Colors

Designer to choose colors to be used in the design.

Requirements
Should not have
• cheep, free

```html
<!DOCTYPE html>
<html lang="en">
<head>
<meta charset="utf-8">
<title>Crestline Painting – Winter Postcard</title>
<link href="https://fonts.googleapis.com/css2?family=Open+Sans:wght@600;700;800&display=swap" rel="stylesheet">
<style>
  :root {
    --ink: #111111;
    --black: #000000;
    --white: #ffffff;
    --red: #e3222a;
    --sky: #b9d3e6;
    --siding: #8f9aa6;
    --rule: #9a9a9a;
    --green: #3a8a3e;
  }
  * { box-sizing: border-box; margin: 0; padding: 0; }
  html, body { width: 1200px; height: 655px; overflow: hidden; background: var(--white); }
  body { font-family: "Open Sans", Arial, sans-serif; }

  .postcard {
    position: relative;
    width: 1200px;
    height: 655px;
    background: var(--white);
    overflow: hidden;
  }

  .headline-band {
    position: absolute;
    left: 0; top: 300px;
    width: 596px; height: 160px;
    background: var(--black);
  }
  .hero {
    position: absolute;
    left: 0; top: 0;
    width: 640px; height: 380px;
  }
  .headline {
    position: absolute;
    left: 0; top: 368px;
    width: 596px;
    color: var(--white);
    font-weight: 700;
    font-size: 36px;
    line-height: 39px;
    text-align: center;
    letter-spacing: -0.3px;
  }

  .question-box {
    position: absolute;
    left: 0; top: 462px;
    width: 268px; height: 131px;
    background: var(--red);
    color: var(--white);
    font-weight: 600;
    font-size: 23px;
    line-height: 27px;
    padding: 11px 8px 0 26px;
    white-space: nowrap;
  }

  .benefits {
    position: absolute;
    left: 280px; top: 464px;
    width: 310px;
    color: var(--ink);
    font-weight: 700;
    font-size: 16.5px;
    line-height: 20px;
    text-align: justify;
  }
  .benefits p + p { margin-top: 9px; }

  .contact-bar {
    position: absolute;
    left: 0; top: 596px;
    width: 596px; height: 59px;
    background: linear-gradient(90deg, var(--black) 0%, var(--black) 65%, var(--white) 82%);
    display: flex;
    align-items: center;
    padding-left: 26px;
    color: var(--white);
    font-weight: 700;
    font-size: 18px;
  }
  .contact-bar .divider {
    width: 3px; height: 26px;
    background: var(--red);
    margin: 0 10px;
  }
  .badges {
    position: absolute;
    right: 14px; top: 10px;
    display: flex; gap: 18px;
  }
  .badge {
    width: 38px; height: 38px;
    border-radius: 50%;
    border: 3px solid var(--red);
    background: var(--white);
  }
  .badge.green { border-color: var(--green); border-radius: 6px; }

  .brand {
    position: absolute;
    left: 500px; top: 66px;
    display: flex; align-items: center; gap: 10px;
  }
  .brand-mark {
    width: 22px; height: 22px;
    background: var(--red);
  }
  .brand-name {
    color: var(--ink);
    font-weight: 800;
    font-size: 34px;
    line-height: 38px;
    text-transform: uppercase;
    letter-spacing: 0.5px;
  }

  .stamp-box {
    position: absolute;
    left: 1003px; top: 27px;
    width: 160px; height: 130px;
    border: 1.5px solid var(--rule);
  }
</style>
</head>
<body>
  <main class="postcard">
    <div class="headline-band"></div>

    <svg class="hero" viewBox="0 0 640 380">
      <defs>
        <linearGradient id="houseTones" x1="0" y1="0" x2="0" y2="1">
          <stop offset="0" stop-color="#b9d3e6"/>
          <stop offset="0.35" stop-color="#a7b3be"/>
          <stop offset="0.7" stop-color="#8f9aa6"/>
          <stop offset="1" stop-color="#6f7a62"/>
        </linearGradient>
      </defs>
      <path role="img" aria-label="Photograph of a grey two-storey house with white trim and front porch"
            d="M0 0 H560 C600 40 598 180 592 290 C420 350 200 350 0 312 Z"
            fill="url(#houseTones)"/>
      <path d="M0 318 C200 356 420 356 596 292" fill="none" stroke="#e3222a" stroke-width="12" stroke-linecap="round"/>
      <path d="M40 340 C240 366 430 352 560 318" fill="none" stroke="#e3222a" stroke-width="4" stroke-linecap="round"/>
      <path d="M430 6 C560 -4 640 60 596 200" fill="none" stroke="#e3222a" stroke-width="10" stroke-linecap="round"/>
      <path d="M470 20 C580 20 620 90 602 170" fill="none" stroke="#ffffff" stroke-width="3" stroke-linecap="round"/>
    </svg>

    <div class="brand">
      <span class="brand-mark"></span>
      <span class="brand-name">Crestline<br>Painting</span>
    </div>

    <h1 class="headline">Have you taken a look around<br>your house this winter?</h1>

    <div class="question-box">Have you noticed<br>any areas of<br>unwanted moisture,<br>mold or draft?</div>

    <div class="benefits">
      <p>Keeping your house painted and well-maintained on the outside will save money in the future as well.</p>
      <p>It protects your home from the elements – whether, wind, rain and snow or the strong summer sun.</p>
    </div>

    <footer class="contact-bar">
      <span class="phone">703-555-0148</span>
      <span class="divider"></span>
      <span class="web">www.crestlinepainting.com</span>
      <div class="badges">
        <span class="badge"></span>
        <span class="badge green"></span>
      </div>
    </footer>

    <div class="stamp-box"></div>
  </main>
</body>
</html>
```